Inspirational Quotes Poster Set

Braxlune is a stylish coworking space, which has a design-oriented vintage look from the 60's with an industrial touch (www.braxlune-example.com) Braxlune Quote Poster Set of 16 posters. The poster should be typo oriented and rather simple. Reflecting a bit the clean billboard design from the sixties. Minimal / simple graphical elements

Target Market(s)

Startups and Entrepreneurs

Industry/Entity Type

Startup

Font styles to use
Sans Serif

Colors

Designer to choose colors to be used in the design.

Requirements
Must have
• Posters need to be on and very stylish

```html
<!DOCTYPE html>
<html lang="en">
<head>
<meta charset="UTF-8">
<title>Braxlune Quote Poster</title>
<link rel="stylesheet" href="https://fonts.googleapis.com/css2?family=Josefin+Sans:wght@600&family=Carlito&display=swap">
<style>
  :root {
    --poster-bg: #c5c7bd;
    --ink: #050505;
  }
  html, body {
    margin: 0;
    padding: 0;
    width: 1200px;
    height: 675px;
    overflow: hidden;
    background: var(--poster-bg);
  }
  .poster {
    position: relative;
    width: 1200px;
    height: 675px;
    background: var(--poster-bg);
    color: var(--ink);
  }
  .quote {
    margin: 0;
    font-family: "Josefin Sans", sans-serif;
    font-weight: 600;
    text-transform: uppercase;
  }
  .quote-line {
    position: absolute;
    left: 0;
    width: 1200px;
    text-align: center;
    font-size: 78px;
    line-height: 1;
    letter-spacing: 0.01em;
    white-space: nowrap;
  }
  .quote-line .initial {
    font-size: 94px;
  }
  .line-1 { top: 52px; left: 6px; }
  .line-2 { top: 184px; }
  .line-3 { top: 296px; }
  .line-4 { top: 428px; }
  .attribution {
    position: absolute;
    left: 0;
    top: 556px;
    width: 1200px;
    margin: 0;
    text-align: center;
    font-family: "Carlito", sans-serif;
    font-size: 58px;
    line-height: 1;
    letter-spacing: 0.02em;
  }
</style>
</head>
<body>
  <main class="poster">
    <blockquote class="quote">
      <div class="quote-line line-1"><span class="initial">Y</span>ou don’t learn to walk</div>
      <div class="quote-line line-2">by following rules</div>
      <div class="quote-line line-3"><span class="initial">Y</span>ou learn by doing</div>
      <div class="quote-line line-4">and falling over.</div>
    </blockquote>
    <p class="attribution">Roland Pemberton, Halcyon Group Founder</p>
  </main>
</body>
</html>
```